Residential Mortgage Leader needs Wordpress Design

Looking for a home page website design for a client. We develop using the WordPress platform and would prefer the design be at least loosely based on an existing WordPress template. Attached files have many notes from our creative brief with client. The site must be responsive. Approved, basic wireframe attached. There is room for interpretation.

Existing web site: http://www.marisolbrandt.example/

The Marisol Brandt Team relies on strong systems to deliver an on-time, done-right, friendly experience. Marisol offers mortgages and refinancing services throughout the United States. She is a successful Keystone Funding agent who strives to be an active part of her community. She would like to focus the site on her team, rather than just her.

Difference makers...
When you work with the Marisol Brandt team you get a high level of expertise and a friendly experience.

She has amazing credentials. Marisol is widely recognized as a top producer for her company, and has earned a number of awards and honors for her customer service.

Marisol's team is very engaged and enjoys sharing social comments or photos from their community.

Imagery:
* Friendly, warm imagery, preferably of her team or an image to represent her team
* Clean and crisp
* Professional / Experts in mortgage and refinance
* Clean / Good use of white space
Updates

When possible, please use imagery from the DFW area. The client mentioned they would prefer not to see stock images. Thanks.

Amend that- creative use of stock images, however, is fine. A few designs have used stock imagery, but in a well-considered manner.

We added some photos and graphics that are local. We are Dallas / Ft. Worth, Plano, Frisco, Texas. We also added some examples of photos to use for the "In the Community" area. Stock photos of business folks just doesn't fit there. Thanks!

Target Market(s)

They service a lot of builders, but also work with homeowners. Their typical client is usually a woman searching for mortgage services online. She typically has a family and may refer her husband to Marisol's team. Keep in mind, however, they also see a number of other scenarios. Most of their clients are middle to high-end borrowers.

Industry/Entity Type

It Company

Requirements
Must have
• Design should be developed using program such as Photoshop or Fireworks or Illustrator as last preference. Ideally, the design would be based on an existing responsive WordPress theme, which we would customize. You must include the name of the target theme. The footer should include lots of space for disclaimers and legal language. Site navigation should include these choices: "Home, About, Builders, Mortgage Info, Approval, Blog, Contact"
Nice to have
• Blog, social media and photos area. Use of the already approved style prototype with colors and fonts (Lato- a Google font, Times New Roman and Cookie-a decorative Google font). However, we are open to interpretation.
Should not have
• Hard to read fonts or a lack of white space.

```html
<!DOCTYPE html>
<html lang="en">
<head>
<meta charset="utf-8">
<title>Keystone Funding – Home</title>
<link rel="stylesheet" href="https://fonts.googleapis.com/css2?family=Lato:wght@300;400;700&family=Oswald:wght@300;400;500&display=swap">
<style>
:root{
  --red:#c2311c;
  --red-dark:#9c2212;
  --charcoal:#3a3a3a;
  --ink:#222;
  --muted:#666;
  --panel:#eef0f4;
  --band:#d9dce3;
  --line:#c8ccd4;
  --white:#fff;
}
*{box-sizing:border-box;margin:0;padding:0}
html,body{width:1200px;height:923px;overflow:hidden;background:var(--white)}
body{position:relative;font-family:Arial,Helvetica,sans-serif;color:var(--ink)}
.abs{position:absolute}

.site-header{left:0;top:0;width:1200px;height:115px;background:linear-gradient(#f3f3f3,#fff)}
.brand{left:155px;top:40px;display:flex;align-items:center;gap:10px}
.brand-name{font-family:Lato,sans-serif;font-weight:700;font-size:31px;color:var(--red);letter-spacing:-.3px}
.brand-mark{width:16px;height:16px;background:var(--red);border-radius:50%}
.brand-tag{left:156px;top:77px;font-family:Lato,sans-serif;font-size:15px;color:#555}
.contact-box{left:889px;top:23px;font-family:Lato,sans-serif;color:#444}
.contact-box .label{font-size:19px;font-weight:300;line-height:22px}
.contact-box .phone{font-size:19px;font-weight:300;line-height:22px}
.contact-box .email{font-size:13px;margin-top:2px}
.contact-box .email a{color:var(--red);text-decoration:none}

.main-nav{left:0;top:115px;width:1200px;height:45px;background:var(--charcoal);border-top:4px solid var(--red)}
.main-nav a{position:absolute;top:3px;height:38px;line-height:38px;font-family:Lato,sans-serif;font-weight:300;font-size:20px;color:#fff;text-decoration:none}
.main-nav a.current{background:var(--red);padding:0 12px;left:139px}
.apply-btn{left:910px;top:105px;width:134px;height:64px;background:linear-gradient(#e0321a,#a91d0d);border-radius:0 0 8px 8px;border-top:10px solid #8e1a0c;color:#fff;font-family:Oswald,sans-serif;font-size:25px;font-weight:400;text-align:center;line-height:52px;box-shadow:0 2px 4px rgba(0,0,0,.3)}

.hero{left:138px;top:173px;width:670px;height:343px;border:1px solid var(--line);background:#fff}
.hero-photo{left:7px;top:7px;width:654px;height:329px;background:linear-gradient(90deg,#f2f3f6 0%,#eceef2 50%,#b9bdc4 75%,#9aa0a8 100%)}
.hero-text{left:24px;top:65px;font-family:Oswald,sans-serif;font-weight:300;font-size:35px;line-height:44.5px;color:#222}

.consult{left:821px;top:174px;width:250px;height:342px;border:1px solid var(--line);background:var(--panel)}
.consult-head{left:821px;top:181px;width:260px;height:41px;background:var(--red);color:#fff;font-family:Lato,sans-serif;font-size:23px;line-height:41px;padding-left:12px}
.consult-fold{left:1071px;top:222px;width:0;height:0;border-top:10px solid #555;border-right:10px solid transparent}
.consult-intro{left:833px;top:238px;font-size:12.5px;line-height:16px;color:#222}
.field{left:834px;width:220px;background:#fff;border:1px solid #ccc;font-family:Lato,sans-serif;font-size:14px;color:#333;padding:2px 8px}
.submit{left:886px;top:460px;width:122px;height:38px;background:#3b3b3b;border:3px solid #fff;outline:1px solid #888;border-radius:4px;color:#fff;font-family:Oswald,sans-serif;font-size:22px;text-align:center;line-height:32px;box-shadow:0 2px 3px rgba(0,0,0,.4)}

.services{left:0;top:535px;width:1200px;height:153px;background:var(--band);border-top:4px solid #c9ccd3}
.services-rule{left:0;top:690px;width:1200px;height:3px;background:#cdd0d6}
.service{width:260px;text-align:center}
.service-icon{position:absolute;width:70px;height:70px;border-radius:50%;background:#fff;box-shadow:3px 3px 0 #9a9da3;display:flex;align-items:center;justify-content:center}
.service h3{font-family:Lato,sans-serif;font-weight:400;font-size:19px;color:#333;margin-top:80px}
.service p{font-size:12.5px;line-height:16px;margin-top:8px}
.more{color:var(--red);font-size:11.5px;text-decoration:none}

.column{width:297px;top:716px;height:220px;border:1px solid var(--line);background:linear-gradient(#eef0f4,#fff 60%)}
.column-head{height:43px;background:var(--red);color:#fff;font-family:Lato,sans-serif;font-size:27px;text-align:center;line-height:45px;border-radius:4px 4px 0 0;margin:-1px -1px 0}
.entry{padding:0 14px}
.entry h4{font-family:Lato,sans-serif;font-weight:400;font-size:17.5px;color:#222;line-height:20px}
.entry p{font-size:12.5px;line-height:15.5px;color:#666}
.award-badge{position:absolute;left:14px;top:93px;width:115px;height:86px;background:#c4c7cc;border:1px solid #aaa}
.award-badge::after{content:"";position:absolute;left:12px;top:18px;width:40px;height:40px;border-radius:50%;background:#6f86b8}
.award-text{position:absolute;left:140px;top:92px;width:150px;font-size:12.5px;line-height:15.5px;color:#666}
</style>
</head>
<body>

<header class="site-header abs">
  <div class="brand abs"><span class="brand-name">Keystone Funding</span><span class="brand-mark"></span></div>
  <div class="brand-tag abs">A Ridgeline Capital Company</div>
  <div class="contact-box abs">
    <div class="label">Work With us:</div>
    <div class="phone">1-800-555-0142</div>
    <div class="email">Email: <a href="#">contact Keystone Funding</a></div>
  </div>
</header>

<nav class="main-nav abs">
  <a class="current" href="#">Home</a>
  <a href="#" style="left:238px">About</a>
  <a href="#" style="left:325px">Builders</a>
  <a href="#" style="left:429px">Mortgage Info</a>
  <a href="#" style="left:584px">Approval</a>
  <a href="#" style="left:696px">Blog</a>
  <a href="#" style="left:772px">Contact</a>
</nav>
<a class="apply-btn abs" href="#" style="text-decoration:none">Apply Now</a>

<section class="hero abs">
  <div class="hero-photo abs" role="img" aria-label="Smiling couple sitting together on the front steps of their home"></div>
  <p class="hero-text abs">We believe in the empowerment<br>that comes through home ownership,<br>and we want to help make this<br>dream come true for you.</p>
</section>

<div class="consult abs"></div>
<h2 class="consult-head abs" style="font-weight:400">Get Free Consultation</h2>
<div class="consult-fold abs"></div>
<p class="consult-intro abs">Ut lobortis erat ac bibendum rutrum.<br>Sed eget iaculis augue.</p>
<div class="field abs" style="top:284px;height:22px">Name</div>
<div class="field abs" style="top:322px;height:22px">Email Address</div>
<div class="field abs" style="top:360px;height:86px;padding-top:6px">Message</div>
<div class="submit abs">SUBMIT</div>

<section class="services abs">
  <div class="service abs" style="left:115px;top:0">
    <div class="service-icon" style="left:90px;top:-12px">
      <svg width="44" height="40" viewBox="0 0 44 40" fill="none" stroke="#c2311c" stroke-width="3.5" stroke-linejoin="round"><path d="M3 20 22 4l19 16"/><path d="M9 16v20h26V16"/><path d="M18 36V25h8v11"/></svg>
    </div>
    <h3>Purchasing a Home?</h3>
    <p>Lorem ipsum dolor sit amet, con-<br>sectetur adipiscing elit <a class="more" href="#">Learn more</a></p>
  </div>
  <div class="service abs" style="left:474px;top:0">
    <div class="service-icon" style="left:90px;top:-12px">
      <svg width="44" height="44" viewBox="0 0 44 44" fill="none" stroke="#c2311c" stroke-width="3"><rect x="8" y="4" width="24" height="34" rx="2"/><text x="11" y="14" font-family="Arial" font-size="8" font-weight="700" fill="#c2311c" stroke="none">LOAN</text><path d="M12 20h14M12 25h12M12 30h8"/><path d="M38 14 26 32l-2 5 4-3L40 16z" fill="#c2311c"/></svg>
    </div>
    <h3>Need to Refinance?</h3>
    <p>Lorem ipsum dolor sit amet, con-<br>sectetur adipiscing elit <a class="more" href="#">Learn more</a></p>
  </div>
  <div class="service abs" style="left:824px;top:0">
    <div class="service-icon" style="left:90px;top:-12px">
      <svg width="44" height="44" viewBox="0 0 44 44" fill="none" stroke="#c2311c" stroke-width="3"><rect x="4" y="6" width="30" height="18" rx="2" stroke-dasharray="4 2"/><text x="14" y="21" font-family="Arial" font-size="14" font-weight="700" fill="#c2311c" stroke="none">$</text><circle cx="24" cy="36" r="4"/><circle cx="36" cy="36" r="4"/><path d="M26 33 36 20M34 33 24 20"/></svg>
    </div>
    <h3>Consolidating Debt?</h3>
    <p>Lorem ipsum dolor sit amet, con-<br>sectetur adipiscing elit <a class="more" href="#">Learn more</a></p>
  </div>
</section>
<div class="services-rule abs"></div>

<section class="column abs" style="left:138px">
  <h2 class="column-head" style="font-weight:400">Our Credentials</h2>
  <div class="entry" style="margin-top:16px">
    <h4>In-House Lending Authority –</h4>
    <p>Lorem ipsum dolor sit amet, consectetur adipi-<br>scing elit <a class="more" href="#">Learn more</a></p>
  </div>
  <div class="entry" style="margin-top:17px">
    <h4>We Fund Our Loans –</h4>
    <p>Lorem ipsum dolor sit amet, consectetur adipi-<br>scing elit. Phasellus eu <a class="more" href="#">Learn more</a></p>
  </div>
  <div class="entry" style="margin-top:17px">
    <h4>Professional, Experienced Staff –</h4>
  </div>
</section>

<section class="column abs" style="left:458px">
  <h2 class="column-head" style="font-weight:400">Awards</h2>
  <div class="entry" style="margin-top:20px"><h4>This is Dummy Heading</h4></div>
  <div class="award-badge" role="img" aria-label="Readers' choice award badge"></div>
  <p class="award-text">Lorem ipsum dolor sit amet, consectetur adipi-scing elit. Phasellus eu sapien at augue aliquam interdum nec a</p>
  <div class="entry" style="position:absolute;top:194px"><h4>This is Dummy Heading</h4></div>
</section>

<section class="column abs" style="left:776px">
  <h2 class="column-head" style="font-weight:400">Recognition</h2>
  <div class="entry" style="margin-top:16px">
    <h4>This is Dummy Heading –</h4>
    <p>Lorem ipsum dolor sit amet, consectetur adipi-<br>scing elit <a class="more" href="#">Learn more</a></p>
  </div>
  <div class="entry" style="margin-top:17px">
    <h4>This is Dummy Heading –</h4>
    <p>Lorem ipsum dolor sit amet, consectetur adipi-<br>scing elit. Phasellus eu <a class="more" href="#">Learn more</a></p>
  </div>
  <div class="entry" style="margin-top:17px">
    <h4>This is Dummy Heading–</h4>
  </div>
</section>

</body>
</html>
```